Tolvek Consulting
Tolvek Consulting stationary
Tolvek Consulting - Consulting
Creative Brief
Professional
Daniel R. Tolvek
Chief Executive Officer
Tolvek Consulting, LLC P.O. Box 4372 Phoenix, AZ 85004
daniel@danielrtolvek-mail.com
danielrtolvek-mail.com
Tolvek Consulting Logo

```html
<!DOCTYPE html>
<html lang="en">
<head>
<meta charset="utf-8">
<title>Tolvek Consulting Stationery</title>
<link href="https://fonts.googleapis.com/css2?family=Exo+2:wght@400;600;700&display=swap" rel="stylesheet">
<style>
:root{
  --bg-dark:#141414;
  --bg-mid:#2c2c2c;
  --navy:#0d2f5c;
  --blue:#1d5fa8;
  --orange:#f29a1f;
  --orange-deep:#e06f12;
  --paper:#ffffff;
  --paper-shade:#e9edf2;
  --ink:#3b4653;
  --label:#8d8d8d;
}
*{margin:0;padding:0;box-sizing:border-box}
html,body{width:1200px;height:397px;overflow:hidden}
body{font-family:"Exo 2",sans-serif;background:radial-gradient(ellipse at 55% 50%,var(--bg-mid),var(--bg-dark) 75%);position:relative}
.brand{position:absolute;left:112px;top:40px;display:flex;align-items:center;gap:14px}
.brand-square{width:34px;height:34px;background:var(--orange)}
.brand-name{font-weight:700;font-size:34px;color:var(--blue);letter-spacing:1px}
.card{position:absolute;border-radius:3px;box-shadow:0 3px 8px rgba(0,0,0,.6);overflow:hidden;padding:8px}
.card .name{font-weight:700;font-size:10px;line-height:1.1}
.card .line{font-size:5px;line-height:1.5;color:var(--ink)}
.card-white{background:var(--paper)}
.card-white .name{color:var(--navy)}
.card-orange{background:linear-gradient(135deg,var(--orange),var(--orange-deep))}
.card-orange .name,.card-orange .line{color:var(--paper)}
.card-navy{background:linear-gradient(135deg,var(--blue),var(--navy))}
.card-navy .name{color:var(--paper)}
.edge{position:absolute;top:0;bottom:0;width:10px;background:var(--navy)}
.label{position:absolute;font-size:6px;color:var(--label);text-transform:uppercase;letter-spacing:1px;text-align:center}
.letterhead{position:absolute;left:742px;top:38px;width:166px;height:318px;background:var(--paper);box-shadow:0 4px 12px rgba(0,0,0,.6);padding:14px 12px}
.letterhead .name{font-weight:700;font-size:11px;color:var(--navy)}
.letterhead .contact{position:absolute;right:12px;top:14px;font-size:4.5px;line-height:1.6;color:var(--ink);text-align:left}
.letterhead .rule{position:absolute;left:12px;right:12px;bottom:16px;height:2px;background:var(--orange)}
.envelopes{position:absolute;left:950px;top:30px}
</style>
</head>
<body>
<div class="brand"><span class="brand-square"></span><span class="brand-name">Tolvek Consulting</span></div>

<div class="card card-white" style="left:100px;top:186px;width:120px;height:68px">
  <div class="line" style="font-weight:600">Daniel R. Tolvek</div>
  <div class="line">Chief Executive Officer</div>
  <div class="name" style="position:absolute;right:8px;top:28px;font-size:9px">Tolvek Consulting</div>
  <div class="line" style="position:absolute;left:8px;bottom:6px">daniel@danielrtolvek-mail.com</div>
</div>
<div class="label" style="left:100px;top:258px;width:120px">Card Front</div>

<div class="card card-white" style="left:236px;top:186px;width:120px;height:68px">
  <div class="edge" style="left:0"></div>
  <div style="padding-left:10px">
    <div class="name" style="font-size:9px">Tolvek Consulting</div>
    <div class="line">P.O. Box 4372 Phoenix, AZ 85004</div>
    <div class="line">danielrtolvek-mail.com</div>
  </div>
</div>
<div class="label" style="left:236px;top:258px;width:120px">Card Back</div>

<div class="card card-orange" style="left:100px;top:300px;width:130px;height:74px">
  <div class="name">Tolvek Consulting</div>
  <div class="line" style="margin-top:22px">Daniel R. Tolvek</div>
  <div class="line">danielrtolvek-mail.com</div>
</div>
<div class="label" style="left:100px;top:380px;width:130px">Orange Front</div>

<div class="card card-white" style="left:238px;top:300px;width:130px;height:74px">
  <div class="name">Tolvek Consulting</div>
  <div class="line" style="margin-top:22px">Daniel R. Tolvek</div>
  <div class="line">daniel@danielrtolvek-mail.com</div>
</div>
<div class="label" style="left:238px;top:380px;width:130px">White Front</div>

<div class="card card-navy" style="left:376px;top:300px;width:130px;height:74px;display:flex;align-items:center;justify-content:center">
  <div class="name" style="font-size:11px">Tolvek Consulting</div>
</div>
<div class="label" style="left:376px;top:380px;width:130px">Navy Back</div>

<div class="letterhead">
  <div class="name">Tolvek Consulting</div>
  <div class="contact">Tolvek Consulting, LLC<br>P.O. Box 4372<br>Phoenix, AZ 85004<br>danielrtolvek-mail.com</div>
  <div class="rule"></div>
</div>
<div class="label" style="left:742px;top:366px;width:166px">Letterhead</div>

<svg class="envelopes" width="250" height="350" viewBox="0 0 250 350" aria-label="Envelopes">
  <g transform="rotate(-8 120 70)">
    <rect x="10" y="20" width="230" height="110" fill="var(--paper)"/>
    <path d="M10 20 H240 V50 Q125 80 10 50 Z" fill="var(--orange)"/>
    <text x="24" y="42" font-family="Exo 2, sans-serif" font-weight="700" font-size="9" fill="var(--paper)">Tolvek Consulting</text>
  </g>
  <g transform="rotate(-3 120 170)">
    <rect x="15" y="120" width="225" height="100" fill="var(--paper-shade)"/>
    <path d="M15 120 L127 175 L240 120" fill="none" stroke="#c9d0d8" stroke-width="1"/>
  </g>
  <rect x="20" y="200" width="220" height="120" fill="var(--paper)"/>
  <path d="M20 200 H240 V228 Q130 255 20 228 Z" fill="var(--navy)"/>
  <text x="32" y="220" font-family="Exo 2, sans-serif" font-weight="700" font-size="9" fill="var(--paper)">Tolvek Consulting</text>
  <text x="32" y="290" font-family="Exo 2, sans-serif" font-size="4.5" fill="var(--ink)">Tolvek Consulting, LLC</text>
  <text x="32" y="297" font-family="Exo 2, sans-serif" font-size="4.5" fill="var(--ink)">P.O. Box 4372 Phoenix, AZ 85004</text>
  <rect x="20" y="314" width="220" height="6" fill="var(--blue)"/>
</svg>
<div class="label" style="left:970px;top:360px;width:220px">Envelope</div>
</body>
</html>
```